Jahresprogramm für kirchliche Organisation
Zielgruppe
Wir sind die Berufungspastoralstelle im Bistum Hallerau der katholischen Kirche. Wir kümmen uns um die Frage nach der Berufung von jungen Menschen zwischen 17-30 Jahren. Unter Berufung verstehen wir die Frage nach dem Plan Gottes für das eigene Leben
Aufgabenstellung
Es geht um eine Designvorlage für eine Jahresprospekt unserer Stelle, die wir leicht wieder ändern oder ergänzen können (Grafikprogrammgrundkenntnisse sind vorhanden), da manche Termine noch nicht letzlich feststehen.
Vom Design darf es sich gerne an unserer Homepage https://www.lebensweg-kompass-hallerau.de/ orientieren.
Wenn möglich gerne im Endformat DIN lang quer (210 x 105 mm)

```html
<!DOCTYPE html>
<html lang="de">
<head>
<meta charset="utf-8">
<title>Jahresprogramm 2022 – Bistum Hallerau</title>
<link rel="stylesheet" href="https://fonts.googleapis.com/css2?family=Oswald:wght@300;400;600&display=swap">
<style>
  :root {
    --page-bg: #ffffff;
    --card-bg: #ffffff;
    --ink: #111111;
    --ink-soft: #5a5a5a;
    --gold: #e2b12c;
    --band-dark: #050505;
    --photo-light: #e9e3dc;
    --photo-mid: #b9a894;
    --photo-dark: #8c7a68;
  }
  * { margin: 0; padding: 0; box-sizing: border-box; }
  html, body {
    width: 1200px;
    height: 675px;
    overflow: hidden;
    background: var(--page-bg);
  }
  .flyer {
    position: absolute;
    left: 153px;
    top: 114px;
    width: 893px;
    height: 448px;
    background: var(--card-bg);
    box-shadow: 0 2px 8px rgba(0,0,0,0.25);
    font-family: "Oswald", sans-serif;
  }
  .flyer__photo {
    position: absolute;
    left: 0;
    top: 0;
    width: 411px;
    height: 414px;
    background:
      radial-gradient(ellipse 30% 55% at 42% 35%, rgba(250,248,244,0.95), rgba(250,248,244,0) 100%),
      radial-gradient(ellipse 80% 40% at 50% 10%, var(--photo-light), rgba(233,227,220,0) 100%),
      linear-gradient(180deg, var(--photo-light) 0%, var(--photo-mid) 45%, var(--photo-dark) 100%);
  }
  .flyer__band {
    position: absolute;
    top: 414px;
    height: 34px;
  }
  .flyer__band--gold { left: 0; width: 411px; background: var(--gold); }
  .flyer__band--dark { left: 411px; right: 0; background: var(--band-dark); }
  .flyer__year {
    position: absolute;
    right: 63px;
    top: 152px;
    transform: translateY(-100%);
    font-weight: 600;
    font-size: 78px;
    line-height: 1;
    color: var(--ink);
    letter-spacing: 0.5px;
  }
  .flyer__motto {
    position: absolute;
    right: 63px;
    top: 158px;
    font-weight: 300;
    font-size: 38px;
    line-height: 1.2;
    color: var(--ink-soft);
    white-space: nowrap;
  }
  .flyer__motto-ref { margin-left: 14px; }
  .partner {
    position: absolute;
    display: flex;
    align-items: center;
    gap: 8px;
    font-weight: 400;
    white-space: nowrap;
    line-height: 1;
  }
  .partner--program {
    left: 454px;
    top: 292px;
    font-size: 30px;
    color: var(--ink);
  }
  .partner--diocese {
    left: 664px;
    top: 302px;
    font-size: 17px;
    letter-spacing: 1px;
    color: var(--ink-soft);
    text-transform: uppercase;
  }
  .partner__square {
    width: 16px;
    height: 16px;
    background: var(--ink-soft);
  }
</style>
</head>
<body>
  <main class="flyer">
    <div class="flyer__photo" role="img" aria-label="Foto: barfüßige Gestalt in weißem Gewand auf einem sandigen Weg im Gegenlicht"></div>

    <h1 class="flyer__year">2022</h1>
    <p class="flyer__motto">Komm und sieh!<span class="flyer__motto-ref">Joh 1,46</span></p>

    <div class="partner partner--program">
      <span class="partner__name">Weg &amp; Ruf</span>
    </div>
    <div class="partner partner--diocese">
      <span class="partner__square"></span>
      <span class="partner__name">Bistum Hallerau</span>
    </div>

    <div class="flyer__band flyer__band--gold"></div>
    <div class="flyer__band flyer__band--dark"></div>
  </main>
</body>
</html>
```